Create a Magazine Ad for an asbestos law firm

we need an 8 X 13 ad to be on the back of a magazine cover. We have the text Attached and want a similar look and feel to our website : www.harborvale-claims.example. The ad should be targeted to white males 55 years or older who are conservative and worked in industry or industrial plants. The main offer is a free case review and trying to get them to call the telephone number.

Target Market(s)

White collar men who worked in industrial plants. Age 55 years or older.

Industry/Entity Type

Legal

Requirements
Must have
• Pictures of white middle class conservative man or man and woman
Nice to have
• look at www.harborvale-claims.example to an. idea of what we are looking for

```html
<!DOCTYPE html>
<html lang="en">
<head>
<meta charset="utf-8">
<title>Harborvale &amp; Reese – Mesothelioma Magazine Ad</title>
<link href="https://fonts.googleapis.com/css2?family=Cinzel:wght@700;800&family=Poppins:wght@400;600;700&family=Oswald:wght@500&display=swap" rel="stylesheet">
<style>
:root{
  --stage:#e4e2df;
  --paper:#d6d5d3;
  --panel:#f1f0ee;
  --ink:#3a2a24;
  --brown:#5a3a2c;
  --band:#4a3c37;
  --white:#ffffff;
  --rule:#3a2a24;
}
*{margin:0;padding:0;box-sizing:border-box}
html,body{width:1104px;height:1200px;overflow:hidden;background:var(--stage)}
.ad{position:absolute;left:183px;top:0;width:738px;height:1200px;background:var(--paper);overflow:hidden;color:var(--ink)}
.plant-photo{position:absolute;left:0;top:0;width:738px;height:800px;background:linear-gradient(180deg,#e3e3e3 0%,#bdbdbd 55%,#cfcfcf 100%)}
.justice-statue{position:absolute;left:500px;top:210px;width:220px;height:440px;background:radial-gradient(ellipse at 50% 45%,#a2704a 0%,#6b4a38 45%,rgba(90,70,60,.35) 75%,rgba(0,0,0,0) 100%)}
.headline{position:absolute;left:40px;top:36px;width:660px;font-family:'Cinzel',serif;font-weight:800;font-size:31px;line-height:1.12;text-transform:uppercase;color:var(--ink)}
.intro{position:absolute;left:40px;top:122px;width:640px;font-family:'Poppins',sans-serif;font-weight:700;font-size:16.5px;line-height:1.3;text-transform:uppercase;color:var(--brown)}
.list{position:absolute;font-family:'Poppins',sans-serif;font-weight:700;font-size:14.5px;line-height:1.5;text-transform:uppercase;color:var(--brown);list-style:disc;padding-left:20px}
.sources{left:52px;top:215px;width:420px}
.offer-band{position:absolute;left:20px;top:320px;width:470px;height:84px;background:var(--band);clip-path:polygon(2% 8%,100% 0,97% 100%,0 92%);display:flex;align-items:center;padding-left:44px;font-family:'Cinzel',serif;font-weight:700;font-size:19px;line-height:1.25;color:var(--white);text-transform:uppercase}
.steps{left:52px;top:420px;width:400px}
.trust-head{position:absolute;left:40px;top:545px;width:450px;font-family:'Cinzel',serif;font-weight:800;font-size:28px;line-height:1.12;text-transform:uppercase;color:var(--ink)}
.trust-copy{position:absolute;left:40px;top:672px;width:660px;font-family:'Poppins',sans-serif;font-weight:600;font-size:14px;line-height:1.4;color:var(--brown)}
.results-panel{position:absolute;left:0;top:790px;width:738px;height:410px;background:var(--panel)}
.results-head{position:absolute;left:330px;top:802px;width:395px;font-family:'Cinzel',serif;font-weight:800;font-size:17px;line-height:1.2;text-transform:uppercase;color:var(--ink)}
.results-copy{position:absolute;left:330px;top:858px;width:390px;font-family:'Poppins',sans-serif;font-size:12.5px;line-height:1.38;color:var(--brown)}
.settlements{position:absolute;left:330px;top:957px;width:390px;border-collapse:collapse;table-layout:fixed}
.settlements td{border:1.5px solid var(--rule);height:52px;text-align:center;vertical-align:middle;padding:3px}
.amount{display:block;font-family:'Cinzel',serif;font-weight:700;font-size:13px;color:var(--ink)}
.source{display:block;font-family:'Oswald',sans-serif;font-weight:500;font-size:9.5px;line-height:1.2;text-transform:uppercase;color:var(--ink)}
.cta{position:absolute;left:330px;top:1072px;width:390px;font-family:'Poppins',sans-serif;font-size:12px;line-height:1.35;color:var(--brown)}
.cta strong{font-weight:700}
.contact{position:absolute;right:22px;display:flex;align-items:center;gap:8px;color:var(--ink)}
.phone{top:1128px;font-family:'Poppins',sans-serif;font-weight:700;font-size:16px}
.web{top:1152px;font-family:'Poppins',sans-serif;font-size:15px}
.firm{top:1176px;font-family:'Oswald',sans-serif;font-weight:500;font-size:14px;text-transform:uppercase;letter-spacing:.3px}
.contact svg{width:14px;height:14px;flex:none}
.attorney-photo{position:absolute;left:18px;top:820px;width:300px;height:380px;background:linear-gradient(180deg,#c9b7a6 0%,#5b4a42 35%,#3b3230 100%);border-radius:140px 140px 0 0}
</style>
</head>
<body>
<main class="ad">
  <div class="plant-photo" role="img" aria-label="Faded black-and-white photo of an industrial plant"></div>
  <div class="justice-statue" role="img" aria-label="Bronze statue of Lady Justice with sword and scales over ink splashes"></div>

  <h1 class="headline">Diagnosed with Mesothelioma, you could be owed compensation</h1>
  <p class="intro">It's very likely you developed this disease through asbestos exposure. Mesothelioma patients are getting multi-million dollar settlements, decades later, from:</p>
  <ul class="list sources">
    <li>Exposure to asbestos products,</li>
    <li>Ex-employers, or</li>
    <li>Talcum baby powder companies.</li>
  </ul>

  <div class="offer-band">We can help you find out if you<br>qualify for a case in minutes.</div>

  <ul class="list steps">
    <li>We'll analyze your situation at no cost</li>
    <li>Determine how much compensation you could be entitled too</li>
    <li>Show you the next steps to get what you're owed</li>
  </ul>

  <h2 class="trust-head">$30 Billion is available in trust for Mesothelioma patients</h2>
  <p class="trust-copy">Tradesmen in many industries were negligently exposed to asbestos materials well into the 1990s. Whether you developed Mesothelioma yourself due to asbestos exposure or you're the surviving family of a lost loved one you could be entitled to significant compensation.</p>

  <div class="results-panel"></div>
  <h2 class="results-head">How much money can people<br>receivefrom a Mesothelioma case?</h2>
  <p class="results-copy">Depending on where you were exposed and a few other factors, you can get a settlement from 6 to 7 figures. Here are a few examples of Mesothelioma Settlements received by our clients. These figures are the total compensation after all attorney fees and expenses are deducted.</p>

  <table class="settlements">
    <tr>
      <td><span class="amount">$6,142,500</span><span class="source">Exposed through heavy duty vehicles</span></td>
      <td><span class="amount">$6,033,510</span><span class="source">Exposed through general contracting</span></td>
      <td><span class="amount">$5,939,010</span><span class="source">Exposed through boat repair</span></td>
    </tr>
    <tr>
      <td><span class="amount">$3,921,750</span><span class="source">Exposed through navy service</span></td>
      <td><span class="amount">$3,600,450</span><span class="source">Exposed through navy service</span></td>
      <td><span class="amount">$2.5 Million</span><span class="source">Exposed from Nordell talcum baby powder.</span></td>
    </tr>
  </table>

  <p class="cta"><strong>Find out if you're Eligible, for FREE, in Minutes.</strong> We'll evaluate your situation and tell you what your case could be worth. <strong>Get your Free evaluation now!</strong></p>

  <div class="contact phone">
    <svg viewBox="0 0 24 24" aria-hidden="true"><path fill="none" stroke="currentColor" stroke-width="2" d="M5 3h4l2 5-3 2a12 12 0 0 0 6 6l2-3 5 2v4a2 2 0 0 1-2 2A17 17 0 0 1 3 5a2 2 0 0 1 2-2z"/></svg>
    CALL 1-000 555 0100
  </div>
  <div class="contact web">
    <svg viewBox="0 0 24 24" aria-hidden="true"><circle cx="12" cy="12" r="9" fill="none" stroke="currentColor" stroke-width="2"/><path fill="none" stroke="currentColor" stroke-width="1.6" d="M3 12h18M12 3c3 3 3 15 0 18M12 3c-3 3-3 15 0 18"/></svg>
    www.harborvale-claims.example
  </div>
  <div class="contact firm">
    <svg viewBox="0 0 24 24" aria-hidden="true"><path fill="currentColor" d="M12 2a7 7 0 0 0-7 7c0 5 7 13 7 13s7-8 7-13a7 7 0 0 0-7-7zm0 9.5A2.5 2.5 0 1 1 12 6.5a2.5 2.5 0 0 1 0 5z"/></svg>
    Harborvale &amp; Reese, LLP, Martin Harlow, Houston, TX
  </div>

  <div class="attorney-photo" role="img" aria-label="Photo of a smiling middle-aged attorney in a dark suit and blue tie"></div>
</main>
</body>
</html>
```